Nimble Path Advert Flyer for TRIVENAPulses magazine

Nimble Path need a 1 A4 Full Page color advertisement created for the upcoming issues featured in the printed magazine. https://www.trivenapulse.com/magazines/September2017/BigData/

Nimblepath.com.au

Your trusted Data & Analytics Partner

Focused Data driven solutions & services provider
Proven experience and trusted technologies

Quorvanta
ZEL
Big Data
Cloud Architecture
Advanced Analytics

```html
<!DOCTYPE html>
<html lang="en">
<head>
<meta charset="utf-8">
<title>Nimble Path – Full Page Advert</title>
<link rel="stylesheet" href="https://fonts.googleapis.com/css2?family=Exo+2:wght@300;400;600;700&display=swap">
<style>
  :root {
    --navy: #15206b;
    --blue: #1f3d9e;
    --blue-bright: #1c55b0;
    --grey-band: #858585;
    --grey-top: #9a9a9b;
    --grey-light: #c9c9cc;
    --white: #ffffff;
    --list-grey: #666666;
    --icon-grey: #7d7d80;
  }
  html, body {
    margin: 0;
    padding: 0;
    width: 926px;
    height: 1200px;
    overflow: hidden;
    background: #d9d9d9;
  }
  .advert {
    position: relative;
    width: 926px;
    height: 1200px;
    overflow: hidden;
    font-family: "Exo 2", sans-serif;
    color: var(--white);
  }
  .advert__shapes {
    position: absolute;
    inset: 0;
    width: 926px;
    height: 1200px;
  }
  .brand {
    position: absolute;
    left: 36px;
    top: 62px;
    margin: 0;
    font-size: 84px;
    font-weight: 600;
    line-height: 1;
    letter-spacing: -1px;
  }
  .offer {
    position: absolute;
    right: 32px;
    top: 706px;
    margin: 0;
    text-align: right;
    font-size: 21px;
    font-weight: 400;
    line-height: 29px;
    letter-spacing: 0.3px;
  }
  .headline {
    position: absolute;
    left: 56px;
    top: 800px;
    margin: 0;
    font-size: 29px;
    font-weight: 400;
    line-height: 38px;
    letter-spacing: 0.5px;
  }
  .technologies {
    position: absolute;
    right: 32px;
    top: 897px;
    margin: 0;
    padding: 0;
    list-style: none;
    text-align: right;
    color: var(--list-grey);
    font-size: 22px;
    line-height: 37.5px;
    letter-spacing: 0.3px;
  }
  .contact {
    position: absolute;
    top: 1016px;
    width: 180px;
    text-align: center;
    font-size: 10.5px;
  }
  .contact__icon {
    display: block;
    width: 76px;
    height: 76px;
    margin: 0 auto 26px;
  }
  .contact--phone { left: 10px; }
  .contact--email { left: 189px; }
  .contact--web { left: 372px; }
</style>
</head>
<body>
<div class="advert">
  <svg class="advert__shapes" viewBox="0 0 830 1170" preserveAspectRatio="none">
    <defs>
      <linearGradient id="blueField" x1="0" y1="0" x2="1" y2="1">
        <stop offset="0" stop-color="#1a3590"/>
        <stop offset="0.5" stop-color="#283a9c"/>
        <stop offset="1" stop-color="#1c56b3"/>
      </linearGradient>
      <linearGradient id="navyBlock" x1="0" y1="0" x2="1" y2="1">
        <stop offset="0" stop-color="#15206b"/>
        <stop offset="1" stop-color="#1d2d86"/>
      </linearGradient>
      <linearGradient id="photoTone" x1="0" y1="0" x2="1" y2="0.6">
        <stop offset="0" stop-color="#e2e3e6"/>
        <stop offset="0.45" stop-color="#b8babf"/>
        <stop offset="0.8" stop-color="#d3d4d8"/>
        <stop offset="1" stop-color="#eeeeef"/>
      </linearGradient>
    </defs>
    <rect class="field" width="830" height="1170" fill="url(#blueField)"/>
    <polygon class="navy-block" points="0,197 75,197 358,715 0,715" fill="url(#navyBlock)"/>
    <polygon class="top-band-grey" points="470,0 830,0 830,147 590,147" fill="var(--grey-top)"/>
    <polygon class="top-band-sheen" points="450,0 480,0 600,147 570,147" fill="#aeb0c4" opacity="0.6"/>
    <polygon class="photo-panel" role="img" aria-label="Photo: a businessman touching a glowing digital interface of data charts and world map"
             points="75,197 645,197 600,147 830,147 830,645 330,645" fill="url(#photoTone)"/>
    <polygon class="top-band-blue" points="0,0 450,0 645,197 0,197" fill="#1c3e9c"/>
    <polygon class="offer-band" points="268,645 830,645 830,830 375,830" fill="var(--grey-band)"/>
    <polygon class="list-panel" points="440,830 830,830 830,1170 630,1170" fill="var(--white)"/>
  </svg>

  <p class="brand">Nimble Path</p>

  <p class="offer">Focused Data driven solutions<br>&amp; services provider<br>Proven experience and trusted technologies</p>

  <h1 class="headline">YOUR<br>TRUSTED DATA<br>&amp; ANALYTICS<br>PARTNER</h1>

  <ul class="technologies">
    <li>Quorvanta</li>
    <li>ZEL</li>
    <li>Big Data</li>
    <li>Cloud Architecture</li>
    <li>Advanced Analytics</li>
  </ul>

  <div class="contact contact--phone">
    <svg class="contact__icon" viewBox="0 0 76 76">
      <circle cx="38" cy="38" r="38" fill="var(--icon-grey)"/>
      <path d="M31 29c1-1 2-1 3 0l2 3c.5 1 .3 1.6-.5 2.3l-1 1c1 2 3 4 5 5l1-1c.7-.8 1.3-1 2.3-.5l3 2c1 1 1 2 0 3l-1.5 1.5c-1.5 1.5-5 .5-8.5-3s-4.5-7-3-8.5z" fill="#fff"/>
    </svg>
    <span>1300 NIMBLEPT (646 253)</span>
  </div>
  <div class="contact contact--email">
    <svg class="contact__icon" viewBox="0 0 76 76">
      <circle cx="38" cy="38" r="38" fill="var(--icon-grey)"/>
      <path d="M27 38l21-9-8 20-3-8z" fill="#fff"/>
    </svg>
    <span>enquiries@nimblepath.com.au</span>
  </div>
  <div class="contact contact--web">
    <svg class="contact__icon" viewBox="0 0 76 76">
      <circle cx="38" cy="38" r="38" fill="var(--icon-grey)"/>
      <g fill="none" stroke="#fff" stroke-width="1.6">
        <circle cx="38" cy="38" r="10"/>
        <ellipse cx="38" cy="38" rx="4.5" ry="10"/>
        <line x1="28" y1="38" x2="48" y2="38"/>
        <line x1="30" y1="33" x2="46" y2="33"/>
        <line x1="30" y1="43" x2="46" y2="43"/>
      </g>
    </svg>
    <span>www.nimblepath.com.au</span>
  </div>
</div>
</body>
</html>
```